2 business Banners for trade show - Transportation industry

Design 2 roll up banners for trade show and career show
-Size: 80 cm X 200 cm each banner
-Will provide text once the design is selected, please use dummy text first. Regarding the text, the first banner will show 6-7 highlights of the company services. The second banner will have around 50 words brief instruction of the company.
-Use the logo in attachment.
-You can use Microgamma font or a similar font Eurostile and Coda in Google Fonts.
-We are looking for simple and clean design and should match the theme colour of the logo.
-You may use the images that align with our business (Such as air cargo transport, ocean cargo transport, on road trucking, rail cargo transport, customs brokerage and e-commerce transport)
-Refer to the company website for more information http://www.vormelfreight.example Note that do NOT follow the design of the website as it will be updated soon.
-Winner will be hired for more works such as web design

Target Market(s)

Business and corporations

Industry/Entity Type

Logistics

Font styles to use
Other font styles liked:
• Microgamma

Requirements
Must have
• -Match the theme colour of the logo in attachment
Nice to have
• -Transportation images that align with the company's services
Should not have
• -Should not contain images of people
• -Should not follow the design of our existing company website

```html
<!DOCTYPE html>
<html lang="en">
<head>
<meta charset="utf-8">
<title>Vormel Freight – Trade Show Roll-up Banner</title>
<link rel="stylesheet" href="https://fonts.googleapis.com/css2?family=Barlow:wght@400;600&display=swap">
<style>
  :root {
    --paper: #ffffff;
    --ink-dark: #3a3a3c;
    --brand-red: #d21f35;
    --brand-red-deep: #a31a25;
    --brand-red-mid: #b91c2c;
    --sky: #d9e8f3;
    --sea: #3f8fae;
    --sea-deep: #2f7893;
    --port-light: #9a8f86;
    --port-dark: #6e5a55;
    --text-light: #ffffff;
  }
  html, body {
    margin: 0;
    padding: 0;
    width: 1200px;
    height: 3000px;
    overflow: hidden;
    background: var(--paper);
  }
  .banner {
    position: relative;
    width: 1200px;
    height: 3000px;
    background: var(--paper);
    font-family: "Barlow", Arial, sans-serif;
  }
  .brand {
    position: absolute;
    top: 150px;
    left: 0;
    width: 1200px;
    display: flex;
    justify-content: center;
    align-items: center;
    gap: 26px;
  }
  .brand-mark {
    width: 56px;
    height: 56px;
    background: var(--brand-red);
  }
  .brand-name {
    font-family: "Barlow", Arial, sans-serif;
    font-weight: 600;
    font-size: 88px;
    line-height: 1;
    letter-spacing: 2px;
    color: var(--ink-dark);
  }
  .hero-photo {
    position: absolute;
    top: 432px;
    left: 0;
    width: 1200px;
    height: 1800px;
    background: linear-gradient(180deg,
      var(--sky) 0%,
      #b9d5e6 5%,
      var(--sea) 8%,
      var(--sea-deep) 30%,
      #5f8797 36%,
      var(--port-light) 48%,
      #8a6c68 65%,
      var(--port-dark) 100%);
  }
  .red-base {
    position: absolute;
    top: 0;
    left: 0;
    width: 1200px;
    height: 3000px;
  }
  .highlights {
    position: absolute;
    top: 2294px;
    left: 128px;
    margin: 0;
    padding: 0;
    list-style: none;
    color: var(--text-light);
  }
  .highlights li {
    height: 92px;
    line-height: 92px;
    font-weight: 400;
  }
  .highlight-major { font-size: 68px; }
  .highlight-minor { font-size: 54px; }
</style>
</head>
<body>
  <main class="banner">
    <header class="brand">
      <span class="brand-mark" aria-hidden="true"></span>
      <span class="brand-name">Vormel Freight</span>
    </header>

    <div class="hero-photo" role="img" aria-label="Aerial photograph of a busy container port with stacked colourful containers, gantry cranes, cargo ships and a blue sea with islands"></div>

    <svg class="red-base" width="1200" height="3000" viewBox="0 0 1200 3000" aria-hidden="true">
      <defs>
        <linearGradient id="redLeft" x1="0" y1="0" x2="1" y2="1">
          <stop offset="0" stop-color="#d21f35"/>
          <stop offset="1" stop-color="#a31a25"/>
        </linearGradient>
        <linearGradient id="redWedge" x1="0" y1="0" x2="1" y2="1">
          <stop offset="0" stop-color="#951720"/>
          <stop offset="1" stop-color="#c21d30"/>
        </linearGradient>
        <linearGradient id="redLower" x1="1" y1="0" x2="0" y2="1">
          <stop offset="0" stop-color="#d21f35"/>
          <stop offset="1" stop-color="#a31a25"/>
        </linearGradient>
      </defs>
      <polygon points="0,1930 540,2190 1200,2520 1200,3000 0,3000" fill="url(#redLeft)"/>
      <polygon points="540,2190 1200,1740 1200,2520" fill="url(#redWedge)"/>
      <polygon points="540,2190 1200,2520 1200,3000 880,3000" fill="url(#redLower)" opacity="0.35"/>
    </svg>

    <ul class="highlights">
      <li class="highlight-major">Lorem Ipsum</li>
      <li class="highlight-minor">Lorem Ipsum</li>
      <li class="highlight-major">Lorem Ipsum</li>
      <li class="highlight-minor">Lorem Ipsum</li>
      <li class="highlight-major">Simply Dummy</li>
      <li class="highlight-minor">Lorem Ipsum</li>
    </ul>
  </main>
</body>
</html>
```